Business Card Design and New Company Logo

I need a business card design and new company logo for a plant nursery. I will be propagating landscape plants from cuttings and growing them locally for resale, locally grown and nurtured plants for zone 5 climate. I would like a design that depicts the growth of shoots to roots .... locally grown and nurtured landscape plants. Healthy, hardy ornamental trees and shrubs for $4.97. Affordable gardening for all.
Updates
Hello Designers,
Thank you for your submissions. I am going to be out of my office until Monday. I will continue to review submitted designs when I can and posting requests for revisions when time permits on my business trip. I should have a decision next week.
Sincerely,
Marla
Sorry for my delay in choosing a design. I had some unforeseen business and personal events culminate at the same time. I will have my decision by the end of this week and update all by Friday March 21. Thank you for your design submissions and your patience.
Marla
Target Market(s)
Home owners
Industry/Entity Type
Landscape
Contact Information for Business Card
Fernwick Hollow Nursery
Marla Quenby
214 Cobble Brook Lane
Larkmere, MA 01999
413-862-3094
Fernwick4Hollow@mailvale.net
Font styles to use
Look and feel
Each slider illustrates characteristics of the customer's brand and the style your logo design should communicate.

```html
<!DOCTYPE html>
<html lang="en">
<head>
<meta charset="utf-8">
<title>Fernwick Hollow Nursery — Business Card</title>
<link rel="stylesheet" href="https://fonts.googleapis.com/css2?family=Dancing+Script:wght@500&family=Dosis:wght@400;500&display=swap">
<style>
  :root {
    --backdrop: #2a2a2c;
    --card-paper: #f7f8f2;
    --card-edge: #e4e6de;
    --brand-green: #1fa653;
    --text-grey: #6f6f6f;
    --text-dark: #555555;
    --bloom-yellow: #f4d35e;
    --bloom-coral: #f29a7a;
    --bloom-teal: #8fd6cf;
    --bloom-green: #b9e08a;
  }
  * { box-sizing: border-box; margin: 0; padding: 0; }
  html, body { width: 1200px; height: 960px; overflow: hidden; }
  body {
    background: var(--backdrop);
    display: flex;
    flex-direction: column;
    align-items: center;
    justify-content: center;
    gap: 56px;
    font-family: "Dosis", "Helvetica Neue", Arial, sans-serif;
  }
  .card {
    position: relative;
    width: 700px;
    height: 400px;
    background: var(--card-paper);
    border: 1px solid var(--card-edge);
    border-radius: 4px;
    box-shadow: 0 10px 28px rgba(0,0,0,.45);
    overflow: hidden;
  }
  .brand-name {
    font-family: "Dancing Script", "Brush Script MT", cursive;
    font-weight: 500;
    color: var(--brand-green);
    white-space: nowrap;
  }
  .address {
    color: var(--text-grey);
    font-size: 17px;
    font-weight: 400;
    letter-spacing: .5px;
    line-height: 1.35;
    text-align: center;
  }

  /* Front */
  .card-front .floral-art {
    position: absolute;
    left: 0; top: 0;
    width: 230px; height: 400px;
  }
  .card-front .heading {
    position: absolute;
    left: 215px; top: 30px;
    width: 430px;
    text-align: center;
  }
  .card-front .brand-name { font-size: 44px; display: block; }
  .card-front .address { margin-top: 2px; }
  .card-front .contact {
    position: absolute;
    right: 40px; bottom: 34px;
    width: 300px;
    color: var(--text-dark);
    font-size: 16px;
    letter-spacing: .4px;
    line-height: 1.65;
  }

  /* Back */
  .card-back {
    display: flex;
    flex-direction: column;
    align-items: center;
    justify-content: center;
  }
  .card-back .logo-lockup {
    display: flex;
    align-items: center;
    gap: 14px;
  }
  .card-back .logo-dot {
    width: 22px; height: 22px;
    border-radius: 50%;
    background: var(--brand-green);
  }
  .card-back .brand-name { font-size: 44px; }
  .card-back .address { margin-top: 2px; }
</style>
</head>
<body>

  <section class="card card-front" aria-label="Business card front">
    <svg class="floral-art" role="img" aria-label="Watercolour illustration of colourful flowers and leaves" viewBox="0 0 230 400" preserveAspectRatio="none">
      <defs>
        <linearGradient id="bloomWash" x1="0" y1="0" x2="0" y2="1">
          <stop offset="0" stop-color="var(--bloom-teal)"/>
          <stop offset=".35" stop-color="var(--bloom-yellow)"/>
          <stop offset=".6" stop-color="var(--bloom-coral)"/>
          <stop offset="1" stop-color="var(--bloom-green)"/>
        </linearGradient>
        <linearGradient id="bloomFade" x1="0" y1="0" x2="1" y2="0">
          <stop offset="0" stop-color="#fff" stop-opacity="1"/>
          <stop offset=".55" stop-color="#fff" stop-opacity=".6"/>
          <stop offset="1" stop-color="#fff" stop-opacity="0"/>
        </linearGradient>
        <mask id="bloomMask">
          <rect width="230" height="400" fill="url(#bloomFade)"/>
        </mask>
      </defs>
      <rect width="230" height="400" fill="url(#bloomWash)" mask="url(#bloomMask)" opacity=".75"/>
    </svg>

    <div class="heading">
      <span class="brand-name">Fernwick Hollow Nursery</span>
      <p class="address">Marla Quenby 214 Cobble Brook Lane Larkmere<br>MA 01999</p>
    </div>

    <div class="contact">
      <p>Phone : 413-862-3094</p>
      <p>E-mail : Fernwick4Hollow@mailvale.net</p>
    </div>
  </section>

  <section class="card card-back" aria-label="Business card back">
    <div class="logo-lockup">
      <span class="logo-dot"></span>
      <span class="brand-name">Fernwick Hollow Nursery</span>
    </div>
    <p class="address">Marla Quenby 214 Cobble Brook Lane Larkmere<br>MA 01999</p>
  </section>

</body>
</html>
```